Sales Deck Redesign for a B2B business selling customer service AI products

We are looking for a redesign of our sales Deck. we are a B2B business selling customer service AI products.

The sales deck is attached, we would like this to be made less "powerpoint" and more "professional expertise in a friendly package".

Our brand standards are attached with details on logos, colours and imagery.

Other examples of inspiration:
-Our website: https://www.velloquin.example/
-Cloudvista imagery - we are a Cloudvista partner, so linking imagery with Cloudvista would help.
-Competitor: https://www.torvinhub.example/
-Velloquin Tallyboard landing page: https://velloquin.tallyquiz.example/

Full image files and AI/PNG files available on request

Slide 17 is a very rough design but if you can create something that is in line with the rest of the deck that would be great

Target Market(s)

Customer service teams and contact centres

Industry/Entity Type

Technology - Cloudvista Ecosystem

Colors
0054AA
0677BA
7BADD7
CADEEF
E8F1F8

Requirements
Must have
• See description and branding doc
Nice to have
Should not have

```html
<!DOCTYPE html>
<html lang="en">
<head>
<meta charset="utf-8">
<title>Velloquin AI – Automated Quality Assurance A.I.</title>
<link rel="stylesheet" href="https://fonts.googleapis.com/css2?family=Archivo:wght@700;800&family=Inter:wght@400;500;600;700&display=swap">
<style>
:root{
  --navy:#2b2a7a;
  --blue:#0677BA;
  --blue-mid:#2e86d0;
  --blue-bright:#3a8fd8;
  --sky:#7BADD7;
  --ice:#CADEEF;
  --mist:#E8F1F8;
  --page:#d3e4f3;
  --ink:#222;
  --muted:#555;
  --white:#fff;
}
*{box-sizing:border-box;margin:0;padding:0}
html,body{width:1200px;height:4147px;overflow:hidden}
body{background:var(--page);font-family:"Inter",Arial,sans-serif;color:var(--ink);position:relative}
.slide{position:absolute;left:44px;width:1112px;height:625px;background:var(--white);overflow:hidden;box-shadow:0 2px 8px rgba(20,50,90,.12)}
.abs{position:absolute}
.accent{position:absolute;height:5px;display:flex;gap:6px}
.accent i{display:block;height:5px;border-radius:3px}
.accent .a1{width:56px;background:var(--navy)}
.accent .a2{width:30px;background:var(--blue-bright)}
.heading{font-family:"Archivo",Arial,sans-serif;font-weight:800;color:var(--navy);font-size:40px;line-height:54px;letter-spacing:.3px;text-transform:uppercase;white-space:nowrap}
.lead{font-size:24px;color:var(--ink)}
.brand{position:absolute;display:flex;align-items:center;gap:8px;font-family:"Archivo",Arial,sans-serif;font-weight:700;color:var(--navy);letter-spacing:2px;white-space:nowrap}
.brand .dot{border:3px solid var(--blue);border-radius:50%}
.footer{position:absolute;bottom:14px;left:44px;right:44px;display:flex;justify-content:space-between;font-size:15px;color:var(--muted)}
.footer b{color:var(--blue);font-size:19px;font-weight:600}
.ticks{position:absolute;list-style:none;font-size:17px;line-height:35px}
.ticks li{position:relative;padding-left:38px}
.ticks li::before{content:"";position:absolute;left:0;top:11px;width:13px;height:13px;border:2px solid var(--blue-bright);border-radius:50%}
.ticks li::after{content:"";position:absolute;left:5px;top:15px;width:5px;height:3px;border-left:2px solid var(--blue-bright);border-bottom:2px solid var(--blue-bright);transform:rotate(-45deg)}
.art{position:absolute}
.robot{background:linear-gradient(160deg,#5fc4f2,#1e8fd3 60%,#135fa8);border-radius:46% 46% 40% 40%}
.stat{position:absolute;left:620px;top:174px;width:259px;height:148px;background:var(--navy);border-radius:8px;color:#fff;text-align:center;padding-top:28px}
.stat .big{font-size:22px;font-weight:700}
.stat .small{font-size:13px;margin-top:6px}
.stat .line{font-size:13px;margin-top:6px}
.stat .line strong{font-size:22px;font-weight:700}
.clients{position:absolute;left:44px;right:44px;top:478px;display:flex;justify-content:space-between;align-items:center}
.clients span{font-size:30px;font-weight:700;color:var(--navy)}
.pain{position:absolute;font-size:17px;line-height:35px;color:var(--muted);white-space:nowrap}
.pain.left{text-align:right}
.xicon{position:absolute;width:56px;height:56px;border-radius:50%;display:flex;align-items:center;justify-content:center}
.xicon.navy{background:var(--navy)}
.xicon.sky{background:var(--blue-bright)}
.fact{position:absolute;width:261px;height:148px;border:1.5px solid var(--navy);border-radius:6px;background:#fff;text-align:center;padding-top:20px;font-size:19px;line-height:30px;color:var(--ink)}
.fact strong{display:block;color:var(--blue);font-size:27px;font-weight:700;line-height:34px}
.card{position:absolute;background:#fff;border-radius:4px;box-shadow:0 2px 10px rgba(0,0,0,.18)}
.card h4{text-align:center;font-size:15px;font-weight:700;color:var(--navy);padding:12px 0 8px}
.tiles{display:grid;grid-template-columns:repeat(3,1fr);gap:4px;padding:0 6px}
.tile{border:1px solid #e3e3e3;height:96px;padding:6px 8px;position:relative}
.tile .t{font-size:10px;color:#555;white-space:nowrap;overflow:hidden}
.tile .v{font-size:34px;text-align:center;margin-top:10px}
.tile .r{position:absolute;bottom:6px;left:8px;font-size:7px;color:var(--blue)}
.teal{color:#1d8a84}.red{color:#c0392b}.orange{color:#f0a94a}
</style>
</head>
<body>

<section class="slide" style="top:55px">
  <div class="brand" style="left:45px;top:122px;font-size:34px"><span class="dot" style="width:46px;height:46px"></span>VELLOQUIN AI</div>
  <div class="accent" style="left:45px;top:267px"><i class="a1"></i><i class="a2"></i></div>
  <h1 class="heading" style="position:absolute;left:45px;top:282px">Automated Quality<br>Assurance A.I.</h1>
  <p class="abs" style="left:45px;top:410px;font-size:20px;line-height:35px">Automate your Quality Assurance and improve<br>your insight by 50x</p>
  <svg class="abs" style="left:530px;top:40px" width="560" height="560" viewBox="0 0 560 560" aria-hidden="true">
    <circle cx="274" cy="276" r="272" fill="var(--navy)"/>
    <circle cx="105" cy="100" r="22" fill="var(--blue-bright)"/>
    <circle cx="462" cy="98" r="26" fill="var(--navy)"/>
  </svg>
  <div class="art" role="img" aria-label="Photo of a smiling woman working on a laptop at home, with the blue assistant robot mascot beside her" style="left:565px;top:78px;width:480px;height:480px;border-radius:50%;background:radial-gradient(circle at 40% 35%,#e9e4df,#b9b2ad 60%,#7c7a86)"></div>
  <div class="art robot" role="img" aria-label="Blue assistant robot mascot" style="left:920px;top:290px;width:150px;height:270px"></div>
  <div class="abs" style="left:576px;top:413px;width:128px;height:128px;border-radius:50%;background:#fff;box-shadow:0 2px 10px rgba(0,0,0,.15);display:flex;align-items:center;justify-content:center">
    <span role="img" aria-label="Cloudvista partner badge" style="width:70px;height:74px;border-radius:6px;background:var(--navy)"></span>
  </div>
</section>

<section class="slide" style="top:733px">
  <div class="accent" style="left:45px;top:40px"><i class="a1"></i><i class="a2"></i></div>
  <div class="brand" style="left:873px;top:40px;font-size:20px"><span class="dot" style="width:30px;height:30px"></span>VELLOQUIN AI</div>
  <h2 class="heading" style="position:absolute;left:45px;top:52px">About Us</h2>
  <p class="abs lead" style="left:45px;top:118px">We take Complexity and bring Clarity</p>
  <ul class="ticks" style="left:45px;top:230px">
    <li>Trusted by companies across the globe to<br>transform their customer service</li>
    <li>Founded by contact centre leaders in 2015</li>
    <li>Cloudvista AppHarbor Partner<br>5 Star-rated listing</li>
  </ul>
  <div class="stat">
    <div class="big">100m+</div>
    <div class="small">AI predictions provided so far by</div>
    <div class="line"><strong>VELO</strong> Our AI Assistant!</div>
  </div>
  <div class="art robot" role="img" aria-label="Blue assistant robot mascot waving" style="left:900px;top:177px;width:170px;height:250px"></div>
  <div class="clients">
    <span>Harbrook</span><span>Qestral</span><span>Mornlea</span><span>Tavipay</span><span>Corvanta</span>
  </div>
  <div class="footer"><span>© Velloquin AI</span><span>Page <b>2</b></span></div>
</section>

<section class="slide" style="top:1413px;background:var(--blue-mid)">
  <svg class="abs" style="left:0;top:0" width="420" height="625" aria-hidden="true"><circle cx="147" cy="246" r="264" fill="#fff"/></svg>
  <div class="art robot" role="img" aria-label="Blue assistant robot mascot with open arms" style="left:50px;top:130px;width:200px;height:245px"></div>
  <div class="brand" style="left:878px;top:40px;font-size:20px;color:#fff"><span class="dot" style="width:30px;height:30px;border-color:#fff"></span>VELLOQUIN AI</div>
  <div class="accent" style="left:479px;top:250px"><i class="a1" style="background:#fff;width:74px"></i><i class="a2" style="background:var(--navy)"></i></div>
  <h2 class="heading" style="position:absolute;left:479px;top:262px;color:#fff">Why you need AI-powered<br>quality assurance</h2>
  <div class="footer" style="color:#fff"><span>© Velloquin AI</span><span>Page <b style="color:#fff">3</b></span></div>
</section>

<section class="slide" style="top:2091px">
  <div class="accent" style="left:45px;top:40px"><i class="a1"></i><i class="a2"></i></div>
  <div class="brand" style="left:873px;top:40px;font-size:20px"><span class="dot" style="width:30px;height:30px"></span>VELLOQUIN AI</div>
  <h2 class="heading" style="position:absolute;left:45px;top:52px">Manual QA lacks insight &amp;<br>wastes resources</h2>
  <svg class="abs" style="left:376px;top:186px" width="360" height="360" aria-hidden="true">
    <circle cx="180" cy="180" r="178" fill="none" stroke="#c9c9c9" stroke-dasharray="4 5"/>
    <circle cx="180" cy="180" r="115" fill="var(--ice)"/>
  </svg>
  <div class="art robot" role="img" aria-label="Blue assistant robot mascot standing" style="left:495px;top:236px;width:120px;height:250px"></div>

  <p class="pain left" style="right:738px;top:213px">On average, only 2% of all cases<br>will be audited</p>
  <p class="pain left" style="right:779px;top:337px">Cases are randomly selected,<br>meaning issues can be missed</p>
  <p class="pain left" style="right:738px;top:462px">Compliance and soft skill risks are only<br>found on randomly selected cases, not<br>the other 98%</p>
  <p class="pain" style="left:764px;top:213px">QA tools are not integrated, or<br>worse... on spreadsheets!</p>
  <p class="pain" style="left:805px;top:337px">Reporting is delayed, with no<br>key reporting/dashboards</p>
  <p class="pain" style="left:764px;top:462px">Feedback training cycles are slow<br>and lack impact</p>

  <svg width="0" height="0" style="position:absolute"><defs><g id="xmark"><circle cx="12" cy="12" r="10" fill="none" stroke="#fff" stroke-width="1.6"/><path d="M7 7l10 10M17 7L7 17" stroke="#fff" stroke-width="2.2" stroke-linecap="round"/></g></defs></svg>
  <span class="xicon sky" style="left:394px;top:218px"><svg width="24" height="24"><use href="#xmark"/></svg></span>
  <span class="xicon navy" style="left:352px;top:342px"><svg width="24" height="24"><use href="#xmark"/></svg></span>
  <span class="xicon sky" style="left:394px;top:468px"><svg width="24" height="24"><use href="#xmark"/></svg></span>
  <span class="xicon navy" style="left:687px;top:218px"><svg width="24" height="24"><use href="#xmark"/></svg></span>
  <span class="xicon sky" style="left:736px;top:342px"><svg width="24" height="24"><use href="#xmark"/></svg></span>
  <span class="xicon navy" style="left:687px;top:468px"><svg width="24" height="24"><use href="#xmark"/></svg></span>
  <div class="footer"><span>© Velloquin AI</span><span>Page <b>4</b></span></div>
</section>

<section class="slide" style="top:2771px">
  <div class="accent" style="left:45px;top:40px"><i class="a1"></i><i class="a2"></i></div>
  <div class="brand" style="left:873px;top:40px;font-size:20px"><span class="dot" style="width:30px;height:30px"></span>VELLOQUIN AI</div>
  <h2 class="heading" style="position:absolute;left:45px;top:52px">Resulting in a lower NPS score,<br>wasted time &amp; risk</h2>
  <p class="abs" style="left:45px;top:172px;font-size:10px;color:#888">*Based on the Average FTE Salary of Contact Centre Agents</p>
  <svg class="abs" style="left:0;top:0" width="1112" height="625" aria-hidden="true" fill="none" stroke="var(--navy)" stroke-width="1.3">
    <path d="M215 410 L330 235 L649 235"/>
    <path d="M275 418 L499 418"/>
    <path d="M215 428 L420 583 L649 583"/>
  </svg>
  <div class="art robot" role="img" aria-label="Blue assistant robot mascot" style="left:100px;top:233px;width:177px;height:298px"></div>
  <div class="fact" style="left:649px;top:161px"><strong>98%</strong>of service cases<br>missed every day</div>
  <div class="fact" style="left:499px;top:306px;width:259px"><strong>3 Months+</strong>delay in QA training for<br>agents</div>
  <div class="fact" style="left:649px;top:438px;height:150px"><strong>£46k+</strong>of wasted spend due to<br>manual effort*</div>
  <div class="footer"><span>© Velloquin AI</span><span>Page <b>5</b></span></div>
</section>

<section class="slide" style="top:3450px">
  <div class="accent" style="left:45px;top:40px"><i class="a1"></i><i class="a2"></i></div>
  <div class="brand" style="left:873px;top:40px;font-size:20px"><span class="dot" style="width:30px;height:30px"></span>VELLOQUIN AI</div>
  <h2 class="heading" style="position:absolute;left:45px;top:52px">Emotion Scoring</h2>
  <ul class="ticks" style="left:45px;top:222px">
    <li>Flag angry customers and prioritise cases<br>accordingly</li>
    <li>Immediate insight to agent and customer emotions</li>
    <li>Informed case insight – no more random selection!</li>
    <li>Easily identify issues for process and training<br>improvements</li>
    <li>Chatbot impact on customer emotion</li>
  </ul>
  <div class="abs" style="left:561px;top:206px;width:103px;height:290px;background:var(--blue-mid)"></div>
  <div class="card" style="left:661px;top:163px;width:374px;height:318px">
    <h4>Agent Emotion</h4>
    <div class="tiles">
      <div class="tile"><div class="t">Agent Anger Emotio...</div><div class="v teal">963</div></div>
      <div class="tile"><div class="t">Agent Urgency Emot...</div><div class="v orange">3.4k</div></div>
      <div class="tile"><div class="t">Agent Frustration E...</div><div class="v teal">2.2k</div></div>
    </div>
  </div>
  <div class="card" style="left:581px;top:264px;width:384px;height:240px">
    <h4>Customer Emotion</h4>
    <div class="tiles">
      <div class="tile"><div class="t">Customer Concern ...</div><div class="v teal">2.6k</div><div class="r">View report</div></div>
      <div class="tile"><div class="t">Customer Happines...</div><div class="v red">2.8k</div><div class="r">View report</div></div>
      <div class="tile"><div class="t">Customer Neutral E...</div><div class="v teal">842</div><div class="r">View report</div></div>
      <div class="tile"><div class="t">Customer Anger Em...</div><div class="v red">1.6k</div><div class="r">View report</div></div>
      <div class="tile"><div class="t">Customer Urgency ...</div><div class="v teal">2.8k</div><div class="r">View report</div></div>
      <div class="tile"><div class="t">Customer Frustratio...</div><div class="v orange">2.5k</div><div class="r">View report</div></div>
    </div>
  </div>
  <div class="art robot" role="img" aria-label="Small blue assistant robot mascot peeking over the dashboard" style="left:922px;top:359px;width:105px;height:153px"></div>
  <div class="footer"><span>© Velloquin AI</span><span>Page <b>6</b></span></div>
</section>

</body>
</html>
```